A4 Single Page Brochure for Private Cloud Offerings

Theme: Futuristic Tech Company

Brightmoor Systems is looking to offer private cloud services for our enterprise customers in Perth-based data-centres that provides our clients with a lower-cost alternative to Nimbra or KLT yielding better performance.

We are looking for a single A4 brochure with a great graphics design theme to promote these services.

We will be providing five tiers:
- Starter
- Growth
- Professional
- Premier
- Elite

Each plan must list on the brochure the Max VMs, CPU cores, Memory and SSD storage allocated. Refer to the uploaded PNG file.

The brochure must list the following selling points:

- Hosted in a local Perth-based TIER3 and TIER4 datacentres
- WA owned hosting - support local
- Low latency - ultra fast local hosting
- Includes Quorra Host Datacentre licensing
- Includes WallHaven Managed Firewalls for Enterprise level threat detection
- Includes all infrastructure maintenance services
- Full self management of VMs through customer portal
- Includes a 1gbps Internet link
- Predictable fixed monthly fee with no dynamic billing
- No additional charges for Storage Transactions, Internet Usage, VM Snapshots, Datacentre Bandwidth Usage and Firewall Traffic Usage.
- Highly available cluster, no single point of failure.
- Pricing is based on 36 months commit
- Yearly rate increases capped to a maximum of Australian CPI
- All plans have 24/7/365 support with dedicated after hours number.
- Managed backup and managed disaster recovery services can be added to plans

Service provided in accordance with our terms and conditions.

We need the ability to EDIT the brochure to adjust pricing after we receive the final project.

Please do not utilise "Pushing the Boundaries of Technology" - our brand is being replaced with "Specialised Consulting". New website is under development but not launched yet.

Target Market(s)

Information Technology Sector

Colors
0054AA
0677BA
7BADD7
CADEEF
E8F1F8

Requirements
Must have
• Theme of Brightmoor is Blue
Should not have
• Extremely stock imagary that just looks "cheap and stock"

```html
<!DOCTYPE html>
<html lang="en">
<head>
<meta charset="utf-8">
<title>Brightmoor Systems – Private Cloud Brochure</title>
<link href="https://fonts.googleapis.com/css2?family=Poppins:ital,wght@0,400;0,600;0,700;1,600&display=swap" rel="stylesheet">
<style>
  :root {
    --backdrop: #6a6a6a;
    --paper: #ffffff;
    --ink: #1b1b1b;
    --navy-deep: #1f2a86;
    --navy: #28318f;
    --royal: #0054aa;
    --sky: #0677ba;
    --glow: #1a80cf;
    --on-dark: #ffffff;
    --mark: #0054aa;
  }
  * { box-sizing: border-box; margin: 0; padding: 0; }
  html, body {
    width: 1200px; height: 1200px; overflow: hidden;
    background: var(--backdrop);
    font-family: "Poppins", Arial, sans-serif;
  }
  .brochure {
    position: absolute; left: 204px; top: 39px;
    width: 792px; height: 1122px;
    background: var(--paper);
    overflow: hidden;
  }
  .brochure__art { position: absolute; inset: 0; width: 100%; height: 100%; }
  .brand {
    position: absolute; left: 420px; top: 72px;
    display: flex; align-items: center; gap: 12px;
  }
  .brand__square { width: 26px; height: 26px; background: var(--mark); }
  .brand__name {
    font-size: 25px; font-weight: 600; color: var(--mark);
    letter-spacing: 1px; text-transform: uppercase; line-height: 1;
  }
  .intro {
    position: absolute; left: 420px; top: 174px; width: 340px;
    font-size: 13.5px; line-height: 1.2; color: var(--ink); text-align: center;
  }
  .tiers {
    position: absolute; left: 580px; top: 336px;
    font-size: 13px; line-height: 1.2; color: var(--ink);
  }
  .tiers__title { font-weight: 600; margin-bottom: 16px; }
  .tiers__list { list-style: none; }
  .selling {
    position: absolute; left: 32px; top: 592px; width: 700px; color: var(--on-dark);
  }
  .selling__title {
    font-size: 36px; font-weight: 600; letter-spacing: 0.5px;
    margin-left: 4px; margin-bottom: 28px;
  }
  .selling__list { list-style: none; font-size: 13.6px; line-height: 21.2px; }
  .terms {
    position: absolute; left: 36px; top: 1044px;
    font-size: 16px; font-weight: 600; font-style: italic; color: var(--on-dark);
  }
</style>
</head>
<body>
<main class="brochure">
  <svg class="brochure__art" viewBox="0 0 600 850" preserveAspectRatio="none" aria-hidden="true">
    <defs>
      <radialGradient id="upperGlow" cx="0.45" cy="0.42" r="0.6">
        <stop offset="0" stop-color="var(--glow)"/>
        <stop offset="0.55" stop-color="#1f4ea6"/>
        <stop offset="1" stop-color="var(--navy-deep)"/>
      </radialGradient>
      <radialGradient id="lowerGlow" cx="0.55" cy="0.35" r="0.75">
        <stop offset="0" stop-color="#2b5cb6"/>
        <stop offset="0.5" stop-color="var(--navy)"/>
        <stop offset="1" stop-color="var(--navy-deep)"/>
      </radialGradient>
    </defs>
    <polygon class="peak-upper" points="235,0 0,355 0,358 107,418 213,232 400,548 600,660 600,650" fill="url(#upperGlow)"/>
    <polygon class="peak-lower" points="0,358 107,418 213,232 400,548 600,660 600,850 0,850" fill="url(#lowerGlow)"/>
    <polyline class="peak-line" points="0,358 107,418 213,232 400,548 600,660" fill="none" stroke="#ffffff" stroke-width="5" stroke-linejoin="miter"/>
  </svg>

  <div class="brand">
    <span class="brand__square"></span>
    <span class="brand__name">Brightmoor Systems</span>
  </div>

  <p class="intro">Brightmoor Systems is looking to offer private cloud services for our enterprise customers in Perth-based data-centres that provides our clients with a lower-cost alternative to Nimbra or KLT yielding better performance.</p>

  <div class="tiers">
    <p class="tiers__title">We will be providing<br>five tiers:</p>
    <ul class="tiers__list">
      <li>- Starter</li>
      <li>- Growth</li>
      <li>- Professional</li>
      <li>- Premier</li>
      <li>- Elite</li>
    </ul>
  </div>

  <section class="selling">
    <h2 class="selling__title">SELLING POINTS:</h2>
    <ul class="selling__list">
      <li>- Hosted in a local Perth-based TIER3 and TIER4 datacentres</li>
      <li>- WA owned hosting - support local</li>
      <li>- Low latency - ultra fast local hosting</li>
      <li>- Includes Quorra Host Datacentre licensing</li>
      <li>- Includes WallHaven Managed Firewalls for Enterprise level threat detection</li>
      <li>- Includes all infrastructure maintenance services</li>
      <li>- Full self management of VMs through customer portal</li>
      <li>- Includes a 1gbps Internet link</li>
      <li>- Predictable fixed monthly fee with no dynamic billing</li>
      <li>- No additional charges for Storage Transactions, Internet Usage, VM Snapshots, Datacentre Bandwidth Usage and Firewall Traffic Usage.</li>
      <li>- Highly available cluster, no single point of failure.</li>
      <li>- Pricing is based on 36 months commit</li>
      <li>- Yearly rate increases capped to a maximum of Australian CPI</li>
      <li>- All plans have 24/7/365 support with dedicated after hours number.</li>
      <li>- Managed backup and managed disaster recovery services can be added to plans</li>
    </ul>
  </section>

  <p class="terms">Service provided in accordance with our terms and conditions.</p>
</main>
</body>
</html>
```